Amber Lark Prints

wall art that with words that inspire and can uplift people in their homes in times when they are down. An ever present presence to inspire that the subconscious takes in and subliminally feeds the home owner with positivity. Quotes... 1)In the morning, devour the prey, in the evening, divide the spoils. 2)Your situation is not your potential, but your potential depends on how you see your situation. 3)It is never too late, if your still here, then there is still time. 4)Busy your mind with the concepts of harmony, health, peace, and good will, and wonders will happen in your life. 5), it is hard to think straight while going around in circles. 6)you have everything you need to proceed. thses are just a few examples.
I would like to have colourful backgrounds. I am starting a online poster store and need a series of beautifully designed words and colours or pictures that go together like a song and it's two elements of words and music.

Target Market(s)

Anybody with a wall that wants an uplifting presence

Industry/Entity Type

Wall art, home decor

Font styles to use
Serif
Other font styles liked:
• stencil, Dead kansas, newspaper headline styles

Requirements
Must have
• I got to put that on my wall, it's amazing
Nice to have
• I am a martial artist, music producer, writer, lyricist that likes to inspire, and I also appreciate nature and beauty, how this can be incorporated into an artistic expression would be ideal elements. maybe also the colours of

```html
<!DOCTYPE html>
<html lang="en">
<head>
<meta charset="utf-8">
<title>Amber Lark Prints — Think Straight</title>
<link rel="stylesheet" href="https://fonts.googleapis.com/css2?family=Bebas+Neue&family=Barlow:wght@400;500&display=swap">
<style>
  :root {
    --poster-red: #e52029;
    --sky-blue: #00aeef;
    --paper-white: #ffffff;
  }
  html, body {
    margin: 0;
    padding: 0;
    overflow: hidden;
    background: var(--poster-red);
  }
  .poster {
    position: relative;
    width: 848px;
    height: 1200px;
    background: var(--poster-red);
    overflow: hidden;
  }
  .headline {
    position: absolute;
    inset: 0;
    width: 848px;
    height: 1200px;
  }
  .headline text {
    font-family: "Bebas Neue", "Oswald", sans-serif;
  }
  .ink-blue { fill: var(--sky-blue); }
  .ink-white { fill: var(--paper-white); }
  .quote {
    position: absolute;
    margin: 0;
    font-family: "Barlow", "Helvetica Neue", sans-serif;
    font-weight: 500;
    font-size: 17px;
    line-height: 23px;
    color: var(--paper-white);
  }
  .quote--mind {
    top: 89px;
    right: 54px;
    text-align: right;
  }
  .quote--potential {
    top: 484px;
    left: 66px;
    text-align: left;
  }
</style>
</head>
<body>
<main class="poster">
  <svg class="headline" viewBox="0 0 848 1200" aria-label="It is hard to think straight while going around in circles">
    <text class="ink-blue" x="68" y="180" font-size="136" textLength="172" lengthAdjust="spacingAndGlyphs">IT IS</text>
    <text class="ink-blue" x="68" y="290" font-size="136" textLength="337" lengthAdjust="spacingAndGlyphs">HARD TO</text>
    <text class="ink-white" x="258" y="648" font-size="552" textLength="529" lengthAdjust="spacingAndGlyphs">THI</text>
    <text class="ink-blue" x="68" y="1030" font-size="557" textLength="452" lengthAdjust="spacingAndGlyphs">NK</text>
    <text class="ink-blue" x="552" y="797" font-size="74" textLength="235" lengthAdjust="spacingAndGlyphs">STRAIGHT</text>
    <text class="ink-white" x="490" y="870" font-size="74" textLength="295" lengthAdjust="spacingAndGlyphs">WHILE GOING</text>
    <text class="ink-white" x="538" y="943" font-size="74" textLength="192" lengthAdjust="spacingAndGlyphs">AROUND</text>
    <text class="ink-blue" x="738" y="943" font-size="74" textLength="47" lengthAdjust="spacingAndGlyphs">IN</text>
    <text class="ink-white" x="230" y="1117" font-size="200" textLength="555" lengthAdjust="spacingAndGlyphs">CIRCLES</text>
  </svg>

  <p class="quote quote--mind">Busy your mind<br>with the concepts of harmony, health,<br>peace, and good will, and wonders will<br>happen in your life.</p>

  <p class="quote quote--potential">Your situation<br>is not your potential,<br>but your potential<br>depends on how you<br>see your situation.</p>
</main>
</body>
</html>
```